Nanna Keyplate, An IT Company Has New Logo, Need Fresh Business Cards

IT company is called Nanna Keyplate and is displayed nicely with the new logo from here on artflock. Would like a fresh business card look that encompasses the idea that we want clients to Cherish Every Gadget. I love the use of circuitry with hearts as endpoints and x's and o's. It needs to have room for my certification logos of which there are 4 and a KMB Alumni log. I am attaching my current card to illustrate how it has always captured attention, but that was in the early stages of business when I was doing more residential work. I am focused on businesses now, so a level of professionalism is necessary. I would also like the card to lend itself well to additional stationary, email signature, ticketing template for my workboard, etc. For the time being, I need the card for an upcoming conference so that work will come later. Color scheme should be that of the new logo. Thank you and I look forward to the designs.

Target Market(s)

Businesses looking for IT services.

Industry/Entity Type

Information Technology

Contact Information for Business Card

Requirements
Must have
• New logo colors and a warm feel. Possibly a tad feminine as I am female, but appealing to males.
Nice to have
• I would like techy, but no too much so. I like friendly and connecting feels. People LOVED my old card and called me because it gave them a warm feeling.

```html
<!DOCTYPE html>
<html lang="en">
<head>
<meta charset="utf-8">
<title>Nanna Keyplate — Business Card</title>
<link rel="stylesheet" href="https://fonts.googleapis.com/css2?family=Nunito:wght@400;600&family=Varela+Round&display=swap">
<style>
  :root {
    --canvas: #ebebeb;
    --card: #f8f8f9;
    --sky: #84c9e8;
    --lime: #c8df7f;
    --rose: #f0a6c9;
    --lilac: #d4a5cc;
    --tagline: #e88cc0;
    --badge: #d9dde2;
    --rule: #9a9a9a;
    --ink: #333333;
    --white: #ffffff;
  }
  html, body {
    margin: 0;
    padding: 0;
    width: 1200px;
    height: 1134px;
    overflow: hidden;
    background: var(--canvas);
  }
  .card {
    position: absolute;
    width: 678px;
    height: 406px;
    background: var(--card);
    box-shadow: 0 6px 18px rgba(0,0,0,0.18);
  }
  .card svg { display: block; width: 100%; height: 100%; }
  .card-front { left: 237px; top: 90px; }
  .card-back  { left: 240px; top: 625px; }

  .service-title { font-family: "Nunito", sans-serif; font-size: 15px; fill: var(--white); }
  .service-list  { font-family: "Nunito", sans-serif; font-size: 12px; fill: var(--white); }
  .contact-line  { font-family: "Nunito", sans-serif; font-size: 11.5px; fill: var(--white); }
  .alumni-label  { font-family: "Nunito", sans-serif; font-weight: 600; font-size: 8px; fill: var(--ink); }
  .brand-name    { font-family: "Varela Round", sans-serif; fill: var(--sky); }
  .brand-tagline { font-family: "Varela Round", sans-serif; fill: var(--tagline); letter-spacing: 1.6px; }
</style>
</head>
<body>

<section class="card card-front" aria-label="Business card front">
  <svg viewBox="0 0 542 325" xmlns="http://www.w3.org/2000/svg">
    <polygon class="accent-top" points="325,0 542,0 542,18 341,18" fill="var(--rose)"/>

    <g class="certification-badges">
      <rect x="27" y="31" width="56" height="17" rx="3" fill="var(--badge)"/>
      <rect x="110" y="28" width="38" height="20" rx="3" fill="var(--badge)"/>
      <circle cx="182" cy="31" r="5" fill="var(--badge)"/>
      <text class="alumni-label" x="198" y="36">KMB Alumni</text>
      <line x1="177" y1="51" x2="228" y2="51" stroke="var(--rule)" stroke-width="0.6"/>
    </g>

    <g class="brand-lockup">
      <text class="brand-name" x="436" y="154" text-anchor="middle" font-size="13.5">Nanna Keyplate</text>
      <text class="brand-tagline" x="436" y="162" text-anchor="middle" font-size="4.2">CHERISH EVERY GADGET</text>
    </g>

    <polygon class="band-services" points="0,123 255,123 310,190 0,190" fill="var(--lime)"/>
    <polygon class="band-contact" points="0,190 370,190 482,325 0,325" fill="var(--sky)"/>

    <text class="service-title" x="24" y="149">computer care &amp; repair</text>
    <text class="service-list" x="36" y="172">desktops, laptop ,tablets</text>

    <g class="contact-details">
      <circle cx="29" cy="261" r="4.5" fill="var(--rose)"/>
      <path d="M27.2 259.2 q0.6 2.8 3.4 3.6" stroke="var(--white)" stroke-width="1" fill="none"/>
      <text class="contact-line" x="39" y="265">407-555-0148</text>

      <circle cx="29" cy="278" r="4.5" fill="var(--lime)"/>
      <rect x="26.6" y="276.4" width="4.8" height="3.3" fill="none" stroke="var(--white)" stroke-width="0.8"/>
      <text class="contact-line" x="39" y="282">nanna.keyplate@mailbox.com</text>

      <circle cx="29" cy="295" r="4.5" fill="var(--rose)"/>
      <circle cx="29" cy="295" r="2" fill="none" stroke="var(--white)" stroke-width="0.8"/>
      <text class="contact-line" x="39" y="299">www.nanna-keyplate.com</text>
    </g>
  </svg>
</section>

<section class="card card-back" aria-label="Business card back">
  <svg viewBox="0 0 543 326" xmlns="http://www.w3.org/2000/svg">
    <polygon class="band-top-sky" points="0,0 313,0 348,48 0,48" fill="var(--sky)"/>
    <polygon class="band-top-lime" points="313,0 378,0 416,48 348,48" fill="var(--lime)"/>

    <g class="brand-lockup">
      <circle cx="271" cy="150" r="9" fill="var(--lilac)"/>
      <text class="brand-name" x="271" y="222" text-anchor="middle" font-size="28">Nanna Keyplate</text>
      <text class="brand-tagline" x="271" y="237" text-anchor="middle" font-size="9">CHERISH EVERY GADGET</text>
    </g>

    <polygon class="band-bottom-rose" points="68,275 198,275 243,326 108,326" fill="var(--rose)"/>
    <polygon class="band-bottom-lilac" points="198,275 543,275 543,326 243,326" fill="var(--lilac)"/>
  </svg>
</section>

</body>
</html>
```